cover arrangement / layout for "The Lantern Shelf Habit"

I want a cover layout (one for e-book, one for paperback) that is professional enough to compete with the likes of the Rolf Whitcombe, Dorian Pelk, Everett Castlemoor and Hugo Varnel's of the world. I have the book title logo, font, and color pallette - but I want some ideas for the cover (front cover only) layout.

I'm attaching the logo (white on transparent background), as well as the "sample" cover I've been using in mockups. I'm not looking for revolutionary designs or new logos, but rather a "cover" (the whole thing) design and arrangement.

Here are the parameters for the cover designs:

• eBook: 1600 x 2560 pixels, 72 ppi, RGB colorspace

• Physical book: 8.5 x 5.5 inches, 300 ppi, CMYK colorspace

For the physical book, if the designers don't extend the artwork to go outside the entire book, no bleeds need to be added.

We'll need the following from the winning designer(s):

1. An editable source file of the cover design, with open layers (AI; PSD); and

2. The fonts used. My brand fonts are Zing Rust Base, and Overpass. Those should be used, however I'm also open to alternative ideas as an additional consideration.

```html
<!DOCTYPE html>
<html lang="en">
<head>
<meta charset="utf-8">
<title>The Lantern Shelf Habit – Cover Spread</title>
<link rel="stylesheet" href="https://fonts.googleapis.com/css2?family=Teko:wght@400;500&family=Oswald:wght@500;700&family=Montserrat:wght@400;700&display=swap">
<style>
  :root {
    --teal: #2598a8;
    --teal-soft: #3aa6b4;
    --teal-pale: #55b6c2;
    --ink: #17343f;
    --white: #ffffff;
    --bill-green: #6fae4a;
    --bill-dark: #3f7f34;
    --photo-warm: #8a4a3e;
    --photo-cool: #4a5660;
  }
  * { margin: 0; padding: 0; box-sizing: border-box; }
  html, body {
    width: 1200px; height: 800px; overflow: hidden;
    background: var(--white);
  }
  .spread {
    position: absolute; left: 80px; top: 15px;
    width: 721px; height: 534px;
    background: var(--teal);
    transform: scale(1.442); transform-origin: top left;
    color: var(--white);
  }
  .spread > * { position: absolute; }

  /* Back cover */
  .author-photo {
    left: 42px; top: 58px; width: 66px; height: 82px;
    background: linear-gradient(135deg, var(--photo-cool), var(--photo-warm));
  }
  .back-author-name {
    left: 116px; top: 55px;
    font: 500 13px/1 "Teko", sans-serif; letter-spacing: 2.6px;
  }
  .author-bio {
    left: 116px; top: 76px; width: 222px;
    font: 400 6.1px/1.55 "Montserrat", sans-serif;
  }
  .back-mark {
    left: 120px; top: 190px; width: 100px;
    text-align: center;
    font: 700 14px/1.05 "Oswald", sans-serif;
  }
  .blurb {
    left: 43px; top: 279px; width: 292px;
    font: 400 6.1px/1.55 "Montserrat", sans-serif;
  }
  .blurb p + p { margin-top: 8px; }
  .blurb strong { font-weight: 700; font-size: 7px; }
  .barcode-panel {
    left: 0; top: 409px; width: 344px; height: 89px;
    background: var(--white);
  }

  /* Spine */
  .spine-title {
    left: 361px; top: 137px;
    writing-mode: vertical-rl;
    font: 400 17px/1 "Teko", sans-serif; letter-spacing: 4.5px;
  }

  /* Front cover */
  .falling-bills {
    left: 462px; top: 0; width: 176px; height: 152px;
    background: linear-gradient(160deg, var(--bill-green), var(--bill-dark));
    opacity: 0.85;
  }
  .jar-art {
    left: 432px; top: 152px; width: 236px; height: 200px;
    background: linear-gradient(180deg, var(--teal-pale), var(--teal-soft));
  }
  .front-title {
    left: 432px; top: 198px; width: 236px;
    text-align: center;
    font: 700 31px/1.05 "Oswald", sans-serif;
    color: var(--white);
  }
  .subtitle {
    left: 447px; top: 370px; width: 200px;
    text-align: center; color: var(--ink);
    font-family: "Oswald", sans-serif; font-weight: 700;
    line-height: 1;
  }
  .subtitle .lead { display: block; font-size: 14px; font-weight: 500; }
  .subtitle .big { font-size: 23px; }
  .subtitle .small { font-size: 14px; font-weight: 500; }
  .subtitle .line { display: block; margin-top: 3px; }
  .front-author-name {
    left: 397px; top: 478px; width: 300px;
    text-align: center;
    font: 500 21px/1 "Teko", sans-serif; letter-spacing: 4.2px;
  }
</style>
</head>
<body>
  <main class="spread">
    <!-- Back cover -->
    <div class="author-photo" role="img" aria-label="Author portrait photograph"></div>
    <h2 class="back-author-name">NOLAN BRIGHTWATER JR</h2>
    <p class="author-bio">Nolan Brightwater is an award-winning keynote speaker who is regularly called upon by global trade associations and business leaders to share his work with their organizations. His Lantern Shelf Habit and Stagehand Method methodologies have been implemented by leading organizations around the world who seek to improve employee engagement, increase employee retention, and build a workforce full of high-performing, highly fulfilled people.</p>
    <div class="back-mark">The Lantern<br>Shelf Habit</div>
    <div class="blurb">
      <p><strong>The Lantern Shelf Habit</strong>: Discover How to Re-engage and Reignite your Workforce offers a piercing critique of the day-to-day experience offered by the modern workplace. It also provides readers with an exciting possibility for a new path forward.</p>
      <p>The world has been plagued by lackluster employee engagement, and average workforce tenure has plummeted over the last two decades. Low morale and high turnover continue to rob organizations of profit and opportunity. But rather than attacking the cause of this crisis, the business world has wasted billions of dollars trying to treat the symptom.</p>
    </div>
    <div class="barcode-panel"></div>

    <!-- Spine -->
    <div class="spine-title">THE LANTERN SHELF HABIT</div>

    <!-- Front cover -->
    <div class="falling-bills" role="img" aria-label="Illustration of dollar bills falling into the jar"></div>
    <div class="jar-art" role="img" aria-label="Illustration of a round glass jar holding the title"></div>
    <h1 class="front-title">The<br>Lantern Shelf<br>Habit</h1>
    <p class="subtitle">
      <span class="lead">HOW TO</span>
      <span class="line"><span class="big">RE-ENGAGE</span> <span class="small">&amp;</span></span>
      <span class="line"><span class="big">RE-IGNITE</span> <span class="small">YOUR</span></span>
      <span class="line"><span class="big">WORKFORCE</span></span>
    </p>
    <div class="front-author-name">NOLAN BRIGHTWATER JR</div>
  </main>
</body>
</html>
```